Business Card, Stationary with Shark Logo for Personal Injury Lawyer

I need business cards and stationery with a shark logo for my Personal Injury Law Practice. Has to have this written on it:
Martin K. Hollis
Injury Lawyer
The Corvell Building
718 Tandy Street
Brookmere, Rhode Island 02944
401-627-4193
Martinhollis.com

Contact Information for Business Card

Martin K. Hollis, Injury Lawyer, address, 401-627-4193, martinhollis.com

```html
<!DOCTYPE html>
<html lang="en">
<head>
<meta charset="utf-8">
<title>Martin K. Hollis – Business Card</title>
<link href="https://fonts.googleapis.com/css2?family=Open+Sans:wght@400;700&display=swap" rel="stylesheet">
<style>
  :root {
    --backdrop: #d9d9db;
    --card-white: #ffffff;
    --navy: #2e2a72;
    --navy-deep: #262262;
    --accent: #3d3399;
    --text-grey: #6b6b6b;
    --divider: #8e89b8;
  }
  * { margin: 0; padding: 0; box-sizing: border-box; }
  html, body {
    width: 1200px; height: 801px; overflow: hidden;
    background: var(--backdrop);
    font-family: "Open Sans", sans-serif;
  }
  .stage {
    position: relative; width: 1200px; height: 801px;
    display: flex; align-items: center; justify-content: center; gap: 60px;
  }
  .card {
    position: relative; width: 500px; height: 286px;
    box-shadow: 0 8px 24px rgba(0,0,0,0.18);
    overflow: hidden;
  }
  .card--front { background: var(--card-white); }
  .identity {
    position: absolute; left: 30px; top: 50%; transform: translateY(-50%);
    white-space: nowrap;
  }
  .identity__name {
    font-weight: 700; font-size: 20px; letter-spacing: 0.4px;
    color: var(--navy-deep); text-transform: uppercase; line-height: 1.15;
  }
  .identity__title { font-size: 15px; color: var(--text-grey); margin-top: 2px; text-align: right; }
  .divider {
    position: absolute; left: 250px; top: 96px; width: 1px; height: 96px;
    background: var(--divider);
  }
  .contact {
    position: absolute; left: 270px; top: 50%; transform: translateY(-50%);
    font-size: 13.5px; line-height: 1.55; color: var(--text-grey);
    font-style: normal; white-space: nowrap;
  }
  .contact__building { color: var(--accent); }
  .contact__line { display: flex; align-items: center; gap: 7px; }
  .contact__line svg { flex: none; }
  .card--back { background: var(--navy); }
  .pattern {
    position: absolute; inset: 0;
    background: linear-gradient(135deg, #35317f 0%, #2e2a72 50%, #26225f 100%);
  }
  .brand {
    position: absolute; right: 30px; top: 50%; transform: translateY(-50%);
    color: #ffffff; font-weight: 700; font-size: 24px; letter-spacing: 0.5px;
    text-transform: uppercase;
  }
</style>
</head>
<body>
<main class="stage">
  <section class="card card--front" aria-label="Business card front">
    <div class="identity">
      <p class="identity__name">Martin K. Hollis</p>
      <p class="identity__title">Injury Lawyer</p>
    </div>
    <div class="divider"></div>
    <address class="contact">
      <p class="contact__building">The Corvell Building</p>
      <p>718 Tandy Street</p>
      <p>Brookmere, Rhode Island 02944</p>
      <p class="contact__line">
        <svg width="11" height="11" viewBox="0 0 12 12" aria-hidden="true"><circle cx="6" cy="6" r="6" fill="#2e2a72"/><path d="M4 3.2c.4-.2.7 0 .9.4l.3.6c.1.3 0 .5-.2.7l-.3.2c.3.7.8 1.2 1.5 1.5l.2-.3c.2-.2.4-.3.7-.2l.6.3c.4.2.6.5.4.9-.3.6-.9.8-1.5.6C5 7.4 4.2 6.6 3.6 5c-.2-.7 0-1.4.4-1.8z" fill="#fff"/></svg>
        401-627-4193
      </p>
      <p class="contact__line">
        <svg width="11" height="11" viewBox="0 0 12 12" aria-hidden="true"><circle cx="6" cy="6" r="6" fill="#2e2a72"/><circle cx="6" cy="6" r="3.6" fill="none" stroke="#fff" stroke-width="0.9"/><path d="M2.4 6h7.2M6 2.4c-1.4 1.8-1.4 5.4 0 7.2M6 2.4c1.4 1.8 1.4 5.4 0 7.2" fill="none" stroke="#fff" stroke-width="0.8"/></svg>
        Martinhollis.com
      </p>
    </address>
  </section>

  <section class="card card--back" aria-label="Business card back">
    <div class="pattern" role="img" aria-label="Tone-on-tone repeating shark fin pattern in navy"></div>
    <p class="brand">Martin K. Hollis</p>
  </section>
</main>
</body>
</html>
```